Stonebridge 720 Real Estate Investment Company

We need a business card designed for a real estate investment company named Stonebridge 720. We want to use red#f04a50, orange #f37122 and yellow #fbee3e as the color scheme. The logo colors will need to be modified from the current blue palette. I've attach VitalBranchly logo example that captures the color scheme we're going for for Stonebridge 720. Looking for clean Sans Serif fonts.
Contact Information for Business Card
Daniel Whitlock
Managing Partner
48613 Kessler Lane, Suite 540
Tampa, FL 33671
813-555-8740 Mobile
dwhitlock@stonebridge720.example
www.stonebridge720.example
Requirements
Must have
- Looking for creative responses.
Nice to have
- Must hit color palette... orange, red, yellow

```html
<!DOCTYPE html>
<html lang="en">
<head>
<meta charset="utf-8">
<title>Stonebridge 720 – Business Card</title>
<link rel="stylesheet" href="https://fonts.googleapis.com/css2?family=Roboto:wght@400;500&family=Roboto+Condensed:wght@700&display=swap">
<style>
  :root {
    --bg: #2a2c2f;
    --card: #0d0d0e;
    --red: #f04a50;
    --orange: #f37122;
    --yellow: #fbee3e;
    --ink: #f2f2f2;
    --muted: #bdbdbd;
  }
  * { box-sizing: border-box; margin: 0; padding: 0; }
  html, body { width: 1200px; height: 900px; overflow: hidden; }
  body {
    background: var(--bg);
    font-family: "Roboto", Arial, sans-serif;
    display: flex;
    align-items: center;
    justify-content: center;
    gap: 48px;
  }
  .card {
    position: relative;
    width: 520px;
    height: 300px;
    background: var(--card);
    border-radius: 22px;
    overflow: hidden;
    box-shadow: 0 14px 30px rgba(0,0,0,.45);
  }

  /* Front */
  .identity { position: absolute; left: 32px; top: 30px; }
  .name {
    font-family: "Roboto Condensed", "Arial Narrow", sans-serif;
    font-weight: 700;
    font-size: 30px;
    line-height: 1;
    color: var(--ink);
  }
  .name .surname { color: var(--red); }
  .role { margin-top: 5px; font-size: 14px; color: var(--muted); }

  .contacts { position: absolute; left: 32px; top: 112px; list-style: none; }
  .contacts li {
    display: flex; align-items: center; gap: 9px;
    font-size: 13.5px; color: var(--ink);
    margin-bottom: 12px;
    white-space: nowrap;
  }
  .icon {
    width: 22px; height: 22px; border-radius: 50%;
    display: flex; align-items: center; justify-content: center;
    flex: none;
  }
  .icon svg { width: 13px; height: 13px; }
  .icon--phone { background: var(--red); }
  .icon--mail { background: var(--orange); }
  .icon--web { background: var(--yellow); }

  .divider {
    position: absolute; left: 322px; top: 170px;
    width: 2px; height: 100px; background: var(--yellow);
  }
  .brand {
    position: absolute; right: 30px; top: 96px;
    display: flex; align-items: center; gap: 10px;
  }
  .brand-dot {
    width: 26px; height: 26px; border-radius: 50%;
    background: var(--orange); flex: none;
  }
  .brand-name {
    font-family: "Roboto Condensed", "Arial Narrow", sans-serif;
    font-weight: 700; font-size: 24px;
    color: var(--orange);
  }
  .address {
    position: absolute; right: 30px; bottom: 30px;
    text-align: right; font-style: normal;
    font-size: 15px; line-height: 1.75; color: var(--ink);
  }

  /* Back */
  .card--back { display: flex; align-items: center; justify-content: center; }
  .back-name {
    font-family: "Roboto Condensed", "Arial Narrow", sans-serif;
    font-weight: 700; font-size: 46px;
    color: var(--yellow);
  }
  .edge-band {
    position: absolute; left: 0; right: 0; bottom: 0; height: 10px;
    display: flex;
  }
  .edge-band span { flex: 1; }
  .edge-band .r { background: var(--red); }
  .edge-band .y { background: var(--yellow); }
  .edge-band .o { background: var(--orange); }
</style>
</head>
<body>

<section class="card card--front">
  <div class="identity">
    <h1 class="name">Daniel <span class="surname">Whitlock</span></h1>
    <p class="role">Managing Partner</p>
  </div>

  <ul class="contacts">
    <li>
      <span class="icon icon--phone"><svg viewBox="0 0 12 12"><rect x="3" y="1" width="6" height="10" rx="1.2" fill="none" stroke="#0d0d0e" stroke-width="1.4"/></svg></span>
      813-555-8740
    </li>
    <li>
      <span class="icon icon--mail"><svg viewBox="0 0 12 12"><rect x="1" y="3" width="10" height="7" fill="#0d0d0e"/><path d="M1 3 L6 7 L11 3" fill="none" stroke="#f37122" stroke-width="1"/></svg></span>
      dwhitlock@stonebridge720.example
    </li>
    <li>
      <span class="icon icon--web"><svg viewBox="0 0 12 12"><circle cx="6" cy="6" r="4.6" fill="none" stroke="#0d0d0e" stroke-width="1.2"/><path d="M1.4 6 H10.6 M6 1.4 V10.6" stroke="#0d0d0e" stroke-width="1"/></svg></span>
      www.stonebridge720.example
    </li>
  </ul>

  <div class="brand">
    <span class="brand-dot"></span>
    <p class="brand-name">Stonebridge 720</p>
  </div>

  <div class="divider"></div>
  <address class="address">
    48613 Kessler Lane<br>
    Suite 540<br>
    Tampa, FL 33671
  </address>
</section>

<section class="card card--back">
  <p class="back-name">Stonebridge 720</p>
  <div class="edge-band"><span class="r"></span><span class="y"></span><span class="o"></span></div>
</section>

</body>
</html>
```